Corporate Brochure Needed for Real Estate Developer

Have a presentation designed "in house" by laypeople that we would like to have redone to appear more professional and polished. Looking for a document template (although the vast majority of the copy from the in house version will likely be used going forward). The new format can include pictures (feel free to use placeholder images from the internet or our website).
We develop residential developments (we do not typically build the houses - although do at one of our current projects - but instead focus on the community design, community amenities (which we build) and install all the infrastructure before selling lots to homebuilders). We've received national acclaim and a number of national and local awards for our projects. More information on our website at www.vantrell.com
Target Market(s)
This presentation will be used to share our history and expertise with people who are unfamiliar with our company. These include financial institutions (banks), institutional investors (pension funds and other large real estate funds), real estate brokers, land owners, etc.
Industry/Entity Type
Residential
Look and feel

```html
<!DOCTYPE html>
<html lang="en">
<head>
<meta charset="utf-8">
<title>Vantrell Brochure Spread</title>
<link href="https://fonts.googleapis.com/css2?family=Arimo:ital,wght@0,400;0,700;1,700&display=swap" rel="stylesheet">
<style>
:root{
  --page-bg:#cddcea;
  --heading-blue:#1f4f9c;
  --text-dark:#1c1c1c;
  --frame-blue:#2458a6;
  --map-fill:#9fb6d2;
  --portrait-fill:#6b6f78;
}
*{margin:0;padding:0;box-sizing:border-box}
html,body{width:1200px;height:773px;overflow:hidden}
body{background:var(--page-bg);font-family:"Arimo",Arial,sans-serif;color:var(--text-dark);position:relative}
.column{position:absolute;top:0}
.col-markets{left:52px;width:300px}
.col-communities{left:436px;width:322px}
.col-team{left:840px;width:330px}
.feature-heading{font-weight:700;font-style:italic;color:var(--heading-blue);font-size:16px;line-height:24px;white-space:nowrap}
.col-markets .feature-heading{text-align:center}
.experience-heading{margin-top:34px}
.market-map{display:block;margin:2px auto 0;width:290px;height:164px}
.focus-heading{margin-top:22px}
.intro-copy{font-size:14px;line-height:19.5px;margin-top:2px}
.market-list{list-style:none;font-size:13.3px;line-height:17.8px;margin-top:2px}
.market-list li{padding-left:16px;position:relative}
.market-list li::before,.project-list li::before{content:"•";position:absolute;left:2px}
.col-communities .feature-heading{margin-top:34px;font-size:14.6px;line-height:23.5px}
.project-name{font-size:12.3px;margin-top:6px;line-height:17px}
.project-list{list-style:none;font-size:12.2px;line-height:17.3px}
.project-list li{padding-left:20px;position:relative}
.community-photo{display:block;width:318px;height:192px;margin:5px 0 8px}
.team-title{margin-top:34px;font-size:17.5px;font-weight:700;color:var(--heading-blue);letter-spacing:.2px}
.member-name{font-size:13px;font-weight:400;color:var(--heading-blue);line-height:16px}
.member-bio{font-size:9.7px;line-height:12.4px}
.portrait{float:left;width:93px;height:130px;margin:2px 8px 4px 0}
.portrait.second{width:86px;height:86px;margin:10px 8px 4px 5px}
.member-name.second{margin-top:3px}
</style>
</head>
<body>

<section class="column col-markets">
  <h2 class="feature-heading experience-heading">Experience operating land/<br>residential development projects<br>across the United States</h2>
  <svg class="market-map" viewBox="0 0 290 164" role="img" aria-label="Map of the United States marking market experience, current projects and company offices">
    <rect x="0" y="0" width="290" height="164" rx="4" fill="var(--map-fill)"/>
  </svg>
  <h2 class="feature-heading focus-heading">Significant experience in California,<br>Arizona, Texas, Florida and metro<br>Washington, DC .</h2>
  <p class="intro-copy">While Vantrell has historically had significant geographical diversity, its operations have been focused on the following major markets:</p>
  <ul class="market-list">
    <li>San Diego</li><li>Orange County</li><li>Riverside County</li><li>San Francisco / Bay Area</li><li>Palm Springs / Coachella Valley</li><li>Phoenix</li><li>Dallas</li><li>Houston</li><li>Austin</li><li>South Padre</li><li>Naples</li><li>Tampa</li><li>Orlando</li><li>West Palm Beach</li><li>Martin County</li><li>Maryland</li><li>Washington, D.C.</li><li>Northern Virginiat</li>
  </ul>
</section>

<section class="column col-communities">
  <h2 class="feature-heading">Vantrell develops communities that<br>are uniquely designed to foster strong<br>neighborhood connections and include a variety<br>of home styles and recreational amenities.</h2>
  <p class="project-name">Ashbrook (Loudoun County, VA)</p>
  <ul class="project-list">
    <li>Located in the heart of Loudoun County, Ashbrook spans over 4,000 acres and is comprised of four distinctive villages interconnected within the framework of a single master-planned community, which will ultimately contain over 2,200 single family detached homes.</li>
    <li>Unique amenity areas for a wide variety of outdoor recreational pursuits, including the Ashbrook Farm, a farm market and farm garden, resort-style pools and clubhouses, miles of nature trails, a dog park, picnic and camping areas, and a sledding hill.</li>
    <li>Voted #1 Community in America in 2013 by National Council of Home Builders.</li>
    <li>Business plan highlights…</li>
    <li>Participating builders……</li>
  </ul>
  <svg class="community-photo" viewBox="0 0 318 192" role="img" aria-label="Photo of a tree-lined residential street with new homes">
    <defs><linearGradient id="streetTone" x1="0" y1="0" x2="0" y2="1"><stop offset="0" stop-color="#b9c6cf"/><stop offset=".55" stop-color="#6f8a5e"/><stop offset="1" stop-color="#5d6462"/></linearGradient></defs>
    <rect x="2.5" y="2.5" width="313" height="187" rx="12" fill="url(#streetTone)" stroke="var(--frame-blue)" stroke-width="5"/>
  </svg>
  <p class="project-name">Seacliff Commons (Huntington Beach, CA)</p>
  <ul class="project-list">
    <li>Seacliff Commons is an upscale, gated community located just three blocks from the Pacific Ocean in Orange County.</li>
    <li>The community offers luxury attached courtyard homes and townhomes designed with a mix of Spanish, Andalusian, Coastal Cottage and Plantation architectural styles.</li>
    <li>Business plan highlights…</li>
  </ul>
</section>

<section class="column col-team">
  <h2 class="team-title">VANTRELL MANAGEMENT TEAM</h2>
  <h3 class="member-name">Daniel Marsh&nbsp; CEO/Managing Member</h3>
  <div class="member-bio">
    <svg class="portrait" viewBox="0 0 93 130" role="img" aria-label="Portrait photo of Daniel Marsh"><rect width="93" height="130" fill="var(--portrait-fill)"/></svg>
    <p>Daniel is the founder of Vantrell Management, LLC and is based in the company's corporate office outside of Boston, MA. He is responsible for all aspects of the operation of Vantrell including managing of the execution of existing assets and sourcing new investment opportunities. In his various roles over the years, Daniel has been responsible for or involved in the acquisition and development of over 100 master-planned residential communities across the United States incorporating over 125,000 residential units and having a total capitalization of over $5.0 billion.</p>
    <p>Prior to forming Vantrell, he was the President of Stonegate Land, the residential land development affiliate of the Stonegate Group, a global real estate private equity investor, where he was responsible for Stonegate's national residential land and investment and development program. Prior to joining SGL in 2005, Daniel was the Chief Operating and former Director of Acquisitions at Meridane, one of the nation's leading master planned community developers, an affiliate of real estate private equity shop Northfield Realty Partners. Earlier he spent two years at Halbrook Sterling &amp; Co., Inc. in the investment banking division focusing on the execution of financing and merger and acquisition assignments.</p>
    <p>Daniel received his B.A. from Ellsworth University in 1993, where he currently serves on the Ardent School of Arts and Sciences Dean's Advisory Board. He is a member of the Land Planning Forum and currently serves as a member of the leadership team for the Community Development Council- Silver Flight.</p>
  </div>
  <h3 class="member-name second">Peter Lindqvist COO</h3>
  <div class="member-bio">
    <svg class="portrait second" viewBox="0 0 86 86" role="img" aria-label="Portrait photo of Peter Lindqvist"><rect width="86" height="86" fill="var(--portrait-fill)"/></svg>
    <p>&nbsp;</p>
    <p>Peter joined Vantrell at its inception and is responsible for underwriting, executing and asset managing residential land investments. From 2008 until the formation of Vantrell, he served as a Vice President at Stonegate Land (the residential land affiliate of the Stonegate Group) where he was responsible for east coast investment underwriting functions and asset management.</p>
    <p>Peter began his real estate career in 2000 with Carrow, Pike &amp; Dunmore in New York as an Associate in the Real Estate Capital Markets Group where he assisted with the disposition, refinancing, restructuring and portfolio optimization of commercial real estate assets. Looking to establish a career focusing on the residential asset class, he later accepted an opportunity to join Hearthline Homes as a Manager of Finance in Chicago, where the company had recently entered the market. Subsequently, Peter joined Brackenridge (an institutional investment firm focused exclusively on residential investments) where he was responsible for due diligence activities on the strategic oversight of a large portion of the firm's Land Banking and Joint-Venture Equity portfolio.</p>
    <p>Peter graduated from the University of Calvert in 1993 with a BBA in Finance and later attended the University of Lakemont where he graduated in 2000 with an MS in Real Estate &amp; Urban Land Economics and an MBA in Accounting/Finance. He also holds an active CPA designation from the State of Illinois.</p>
  </div>
</section>

</body>
</html>
```